Stationery Set for Brelvo Company

I need to create full stationery design for my company; Business Cards, Envelops, Letter Heads, Calendar.
In the letter head and Envelops... only contact information and website links.
Our company is a Service Management company with different domains of innovative services including Technology Service Management, Education Services, Outsourcing Management, Events Management.
I need a modern and innovative design specially for the business card. I some transparent designs and I like it, but don't limit your innovation to what I mentioned. Sky is limit for your innovation.

Target Market(s)

Middle East & Africa

Industry/Entity Type

Business Management

Colors
34a7d8
0355a3
85acd3
86cae7
cee9f5
cfdeed
e4daeb
f3f1f8
ecf7fb

Requirements
Must have
• Name, Title, Email, Mobile
Nice to have
• We have multiple locations in USA, KSA, EGY, so I need ideas about how to include all contact details maybe QR / Barcode or something else.
• Please see our locations and contact information: www.gofarnix.example
Should not have
• Too much text

```html
<!DOCTYPE html>
<html lang="en">
<head>
<meta charset="utf-8">
<title>Brelvo Company — Business Card</title>
<link href="https://fonts.googleapis.com/css2?family=Arimo:wght@400;700&display=swap" rel="stylesheet">
<style>
  :root {
    --brand-blue: #4373be;
    --ink: #222222;
    --paper: #ffffff;
    --backdrop: #d9dbe0;
  }
  * { margin: 0; padding: 0; box-sizing: border-box; }
  html, body { width: 1200px; height: 750px; overflow: hidden; }
  body {
    background: var(--backdrop);
    font-family: "Arimo", Arial, sans-serif;
    color: var(--ink);
    position: relative;
  }
  .card {
    position: absolute;
    width: 540px;
    height: 310px;
    background: var(--paper);
    box-shadow: 0 6px 18px rgba(0,0,0,0.18);
    overflow: hidden;
  }
  .card--front { left: 40px; top: 220px; display: flex; align-items: center; justify-content: center; }
  .card--back { left: 620px; top: 220px; }

  .brand-name {
    font-weight: 700;
    color: var(--brand-blue);
    font-size: 34px;
    letter-spacing: 0.5px;
  }

  .band {
    position: absolute;
    left: 0; top: 0;
    width: 100%;
    height: 130px;
  }
  .band__shape { position: absolute; inset: 0; }
  .holder {
    position: absolute;
    left: 26px; top: 66px;
    color: var(--paper);
  }
  .holder__name { font-size: 19px; font-weight: 700; }
  .holder__title { font-size: 14px; margin-top: 3px; }
  .card--back .brand-name {
    position: absolute;
    right: 26px; top: 22px;
    font-size: 24px;
    color: var(--brand-blue);
  }

  .offices {
    position: absolute;
    left: 56px; top: 150px;
    font-size: 12.5px;
    line-height: 15px;
    font-style: normal;
  }
  .office__region { color: var(--brand-blue); margin-top: 4px; }
  .office__region:first-child { margin-top: 0; }

  .contacts {
    position: absolute;
    right: 22px; top: 150px;
    list-style: none;
    font-size: 12.5px;
    line-height: 18px;
    text-align: right;
  }
  .contacts li { display: flex; justify-content: flex-end; align-items: center; gap: 8px; }
  .contacts svg { width: 12px; height: 12px; fill: var(--brand-blue); flex: none; }
</style>
</head>
<body>

  <section class="card card--front" aria-label="Card front">
    <span class="brand-name">Brelvo Company</span>
  </section>

  <section class="card card--back" aria-label="Card back">
    <div class="band">
      <svg class="band__shape" viewBox="0 0 540 130" preserveAspectRatio="none" aria-hidden="true">
        <polygon points="0,40 540,0 540,72 0,130" fill="var(--brand-blue)"/>
      </svg>
      <div class="holder">
        <p class="holder__name">Samir Okoro</p>
        <p class="holder__title">President</p>
      </div>
    </div>
    <span class="brand-name">Brelvo Company</span>

    <address class="offices">
      <p class="office__region">USA</p>
      <p>48 Harbor Lane</p>
      <p>6th Floor Maple Ridge</p>
      <p>CA 90000 US</p>
      <p class="office__region">SAUDI ARABIA</p>
      <p>Riyadh, Qasr District,</p>
      <p>Nakheel Road</p>
      <p>Tamra Buildings</p>
      <p>Wing C 3rd Floor Suite 7, 9</p>
    </address>

    <ul class="contacts">
      <li>+1.555.010.2470 (USA)
        <svg viewBox="0 0 24 24"><path d="M6.6 10.8a15.1 15.1 0 0 0 6.6 6.6l2.2-2.2c.3-.3.7-.4 1-.2 1.1.4 2.3.6 3.6.6.6 0 1 .4 1 1V20c0 .6-.4 1-1 1A17 17 0 0 1 3 4c0-.6.4-1 1-1h3.5c.6 0 1 .4 1 1 0 1.3.2 2.5.6 3.6.1.3 0 .7-.2 1z"/></svg>
      </li>
      <li>+966 5550 12 34 (Saudi Arabia)
        <svg viewBox="0 0 24 24"><path d="M6.6 10.8a15.1 15.1 0 0 0 6.6 6.6l2.2-2.2c.3-.3.7-.4 1-.2 1.1.4 2.3.6 3.6.6.6 0 1 .4 1 1V20c0 .6-.4 1-1 1A17 17 0 0 1 3 4c0-.6.4-1 1-1h3.5c.6 0 1 .4 1 1 0 1.3.2 2.5.6 3.6.1.3 0 .7-.2 1z"/></svg>
      </li>
      <li>+1.555.010.2470
        <svg viewBox="0 0 24 24"><path d="M7 1h10a2 2 0 0 1 2 2v18a2 2 0 0 1-2 2H7a2 2 0 0 1-2-2V3a2 2 0 0 1 2-2zm0 3v14h10V4zm5 15.5a1 1 0 1 0 0 2 1 1 0 0 0 0-2z"/></svg>
      </li>
      <li>info@gofarnix.example
        <svg viewBox="0 0 24 24"><path d="M2 5h20v14H2zm2 2v.4l8 5 8-5V7zm0 2.8V17h16V9.8l-8 5z"/></svg>
      </li>
      <li>www.gofarnix.example
        <svg viewBox="0 0 24 24"><path d="M12 2a10 10 0 1 0 0 20 10 10 0 0 0 0-20zm6.9 9h-3a15 15 0 0 0-1.3-6A8 8 0 0 1 18.9 11zM12 4c.9 1.3 1.7 3.8 1.9 7h-3.8c.2-3.2 1-5.7 1.9-7zM9.4 5a15 15 0 0 0-1.3 6h-3A8 8 0 0 1 9.4 5zM5.1 13h3a15 15 0 0 0 1.3 6A8 8 0 0 1 5.1 13zM12 20c-.9-1.3-1.7-3.8-1.9-7h3.8c-.2 3.2-1 5.7-1.9 7zm2.6-1a15 15 0 0 0 1.3-6h3a8 8 0 0 1-4.3 6z"/></svg>
      </li>
    </ul>
  </section>

</body>
</html>
```